*YO!!! Designers Needed!!* Front Page Cover Needed for a $$Billion Dollar$$ Company

We are a manufacturer of aluminum electrolytic capacitors. We are looking to create a front page cover that will be used on our annual report. We are a publicly listed company and work with many Pinnacle 300 companies, so your work will be viewed by the BIG GUNS and EXECUTIVES around the WORLD! If selected, you may be selected for additional work.

The front page cover should be unique. If elegance, modern, bling, and creativity somehow got together and had a child, that's what the cover page would look like!

Inspired Examples attached. Check them out!

www.velmoro.com

Font styles to use
Sans Serif

Requirements
Must have
• 1. Must include the attached logo. Logo size, color, and placement are at your discretion.

2. Should include the text, '2020 Annual Report'

3. The design should incorporate the use of foil and/or be embossed. The foil can be part of the design or can be the full page. See various examples attached for reference.

4. Shall be in A4 size and vertical orientation.
Nice to have
• Feel free to add any icons or stock photos (for example capacitors or circuit boards) if needed.

Be creative here and don't be afraid to be bold! The end product will be printed and budget is not a limiting factor, so feel free to make it extravagant if needed.

Our slogan is "Think Ahead". This slogan can or cannot be part of the theme.

```html
<!DOCTYPE html>
<html lang="en">
<head>
<meta charset="UTF-8">
<title>Velmoro 2020 Annual Report Cover</title>
<link rel="stylesheet" href="https://fonts.googleapis.com/css2?family=Montserrat:wght@400;600;700;800;900&display=swap">
<style>
  :root {
    --paper: #ffffff;
    --navy: #24307a;
    --indigo: #2f3c8f;
    --teal: #27b3a6;
    --ink: #1f2a44;
    --foil-light: #eceef1;
    --foil-mid: #c4c8ce;
    --emboss: #eef0f2;
  }
  * { margin: 0; padding: 0; box-sizing: border-box; }
  html, body {
    width: 900px; height: 1200px; overflow: hidden;
    background: var(--paper);
    font-family: "Montserrat", sans-serif;
  }
  .cover {
    position: relative;
    width: 900px; height: 1200px;
    background: var(--paper);
  }
  .brand {
    position: absolute; left: 110px; top: 95px;
    display: flex; flex-direction: column;
  }
  .brand-name {
    display: flex; align-items: center; gap: 12px;
    font-weight: 800; font-size: 52px; color: var(--ink);
    letter-spacing: 1px; line-height: 1;
  }
  .brand-mark { width: 16px; height: 16px; background: var(--teal); }
  .brand-tagline {
    margin-top: 8px; margin-left: 28px;
    font-size: 11px; font-weight: 600; letter-spacing: 3px;
    color: var(--ink);
  }
  .slogan {
    position: absolute; left: 100px; top: 220px;
    line-height: 0.9;
  }
  .slogan-think {
    display: block;
    font-weight: 700; font-size: 118px; color: var(--indigo);
    letter-spacing: 2px;
  }
  .slogan-ahead {
    display: block;
    font-weight: 900; font-size: 150px; color: var(--teal);
    letter-spacing: 2px;
  }
  .foil-area {
    position: absolute; left: 170px; top: 480px;
    width: 730px; height: 510px;
    background: linear-gradient(105deg, var(--foil-mid) 0%, var(--foil-light) 40%, var(--foil-mid) 75%, var(--foil-light) 100%);
  }
  .report-title {
    position: absolute; left: 170px; top: 480px;
    width: 730px; height: 510px;
    display: flex; flex-direction: column; align-items: center; justify-content: center;
    text-align: center; line-height: 0.95;
    font-weight: 900; color: var(--emboss);
    text-shadow: 2px 2px 2px rgba(60,64,72,0.5), -1px -1px 1px rgba(255,255,255,0.9);
  }
  .report-stack { transform: rotate(-10deg); }
  .report-year { display: block; font-size: 110px; letter-spacing: 4px; }
  .report-label { display: block; font-size: 72px; letter-spacing: 3px; }
  .footer-band {
    position: absolute; left: 0; top: 1010px;
    width: 900px; height: 64px;
    background: var(--navy);
    display: flex; align-items: center; justify-content: center;
  }
  .footer-url {
    color: var(--paper); font-size: 18px; font-weight: 600;
    letter-spacing: 8px;
  }
</style>
</head>
<body>
  <main class="cover">
    <header class="brand">
      <div class="brand-name"><span>Velmoro</span><span class="brand-mark"></span></div>
      <div class="brand-tagline">THINK AHEAD</div>
    </header>

    <h1 class="slogan">
      <span class="slogan-think">THINK</span>
      <span class="slogan-ahead">AHEAD</span>
    </h1>

    <div class="foil-area" role="img" aria-label="Silver aluminium foil sheet unrolling from a roll"></div>

    <h2 class="report-title">
      <span class="report-stack">
        <span class="report-year">2020</span>
        <span class="report-label">ANNUAL</span>
        <span class="report-label">REPORT</span>
      </span>
    </h2>

    <footer class="footer-band">
      <span class="footer-url">www.velmoro.com</span>
    </footer>
  </main>
</body>
</html>
```